Velvora Style & Image Consultancy

Hi, I need a brochure design for my personal styling business. I have downloaded the company logo along with the content of the services offered for the brochure. Being a colour and styling business I would been keen on having some pictures of timeless fashion or colour samples, This is not absolutely necessary just an idea. I had also thought about changing and naming the services offered with a feminine, fun interesting type of theme. This may make it more inviting, I would be really interested in any of your creative ideas in this area. I will be deciding on the business card design in the next couple of days. I will download the design for this once I have made the decision. I will be okay to pay for any photo images that may be required if the brochure is selected. I had envisaged a tri fold brochure standard letter size with two folds (8.5" by 11inchs) however I am open to any suggestions. Please feel free to make any changes or modification's to the content, font etc in the files downloaded for the brochure. Many Thanks.
Updates
Project Deadline Extended
Reason: I need to extend the time for this project as I do not have all of content required for the brochure confirmed. Many Thanks
Industry/Entity Type
Fashion
Font styles to use
Look and feel
Each slider illustrates characteristics of the customer's brand and the style your logo design should communicate.

```html
<!DOCTYPE html>
<html lang="en">
<head>
<meta charset="utf-8">
<title>Velvora Style &amp; Image Consultancy – Brochure</title>
<link rel="stylesheet" href="https://fonts.googleapis.com/css2?family=Caveat+Brush&family=Raleway:wght@300;400;600;700&display=swap">
<style>
  :root{
    --ink:#000000;
    --paper:#ffffff;
    --orange:#fbae2f;
    --pink:#e6007e;
    --teal:#2bb3c8;
    --teal-deep:#1c9fb6;
    --gold-top:#c9a33c;
    --gold-bottom:#a67a28;
    --band:#4a4a4a;
    --dark-text:#1a1a1a;
    --cream:#fff6df;
  }
  *{margin:0;padding:0;box-sizing:border-box}
  html,body{width:1200px;height:927px;overflow:hidden;background:var(--ink)}
  .brochure{position:relative;width:1200px;height:927px;overflow:hidden;background:var(--ink);color:var(--paper);
    font-family:"Raleway",Arial,sans-serif;font-weight:300}
  .panel{position:absolute;top:0;height:927px}
  .panel--left{left:0;width:400px}
  .panel--middle{left:400px;width:401px;background:linear-gradient(180deg,var(--gold-top) 40%,var(--gold-bottom) 100%)}
  .panel--right{left:801px;width:399px}

  .script-title{font-family:"Caveat Brush",cursive;font-weight:400;color:var(--orange);font-size:31px;line-height:1;position:absolute;white-space:nowrap}
  .copy{position:absolute;font-size:10.8px;line-height:16.2px;text-align:justify;letter-spacing:-0.1px}
  .copy p{margin:0}
  .dot{color:var(--pink)}
  .list{list-style:none}
  .list li::before{content:"• ";color:var(--pink)}
  .gap{height:16px}

  /* left */
  .panel--left .script-title{left:31px}
  .panel--left .copy{left:31px;width:345px}

  /* middle */
  .hero-photo{position:absolute;left:0;top:0;width:401px;height:360px;
    background:radial-gradient(ellipse at 50% 55%,#e9e2d6 0%,#d9cdb9 18%,var(--teal) 42%,var(--teal-deep) 100%)}
  .hero-wave{position:absolute;left:0;top:325px;width:401px;height:60px}
  .packages-title{position:absolute;left:30px;top:388px;font-family:"Caveat Brush",cursive;font-size:31px;color:var(--dark-text);line-height:1;white-space:nowrap}
  .packages{position:absolute;left:30px;top:432px;width:348px;font-size:10.6px;line-height:16px;color:var(--cream);text-align:justify;letter-spacing:-0.1px}
  .package h3{font-size:11px;font-weight:700;color:var(--dark-text);margin:0;letter-spacing:0}
  .package ul{list-style:none}
  .package li::before{content:"• ";color:var(--dark-text)}
  .package + .package{margin-top:16px}
  .package--compact{line-height:13.3px}
  .package--compact h3{line-height:16px}

  /* right */
  .panel--right .script-title{left:20px;top:34px}
  .services{position:absolute;left:20px;top:71px;width:345px;font-size:10.7px;line-height:19.1px;text-align:justify;letter-spacing:-0.15px}
  .services h3{color:var(--pink);font-weight:700;font-size:11px;margin-top:3px;letter-spacing:0}
  .services .list li{line-height:19.1px}

  .brand-mark{position:absolute;left:60px;top:864px;display:flex;align-items:center;gap:10px}
  .brand-mark__circle{width:26px;height:26px;border-radius:50%;background:var(--gold-top);flex:none}
  .brand-mark__name{font-family:"Raleway",Arial,sans-serif;font-weight:700;font-size:17px;color:var(--gold-top);line-height:1.2;white-space:nowrap}
</style>
</head>
<body>
<main class="brochure">

  <section class="panel panel--left">
    <h2 class="script-title" style="top:34px">Personal Styling Services</h2>
    <div class="copy" style="top:78px">
      <p><span class="dot">•</span> Colour Analysis- you will discover your colours and how to wear them with confidence.</p>
      <p><span class="dot">•</span> Image &amp; Style Consultation – Express your image &amp; personality through the clothes that you wear and how you wear them. Learn how to select fabrics and clothing styles that will suit &amp; flatter your shape, and how to coordinate them.</p>
      <p><span class="dot">•</span> Wardrobe Make over- Clear out and reassess your wardrobe to ensure it reflects your life style &amp; personality.</p>
      <p><span class="dot">•</span> Style Me Complete Accessories &amp; Pulling it all together,-add the finishing touches to your look with the choice of shoes and accessories, your hair style &amp; make up</p>
      <div class="gap"></div>
      <ul class="list">
        <li>Personal Shopping</li>
        <li>Make up Lessons</li>
        <li>Special Occasion Make up</li>
        <li>Seasonal Review &amp; Update</li>
        <li>Party &amp; Group Experiences</li>
        <li>Complete Makeovers</li>
        <li>Personal Styling Packages</li>
      </ul>
    </div>

    <h2 class="script-title" style="top:462px">Velvora color consultation</h2>
    <div class="copy" style="top:507px">
      <p>Colour has a huge impact on the way we look and how we feel. Wearing colours that compliment us help us appear vibrant; your eyes will sparkle, giving you a more youthful and healthier appearance.</p>
      <p>During an individual colour consultation you will discover</p>
      <p><span class="dot">•</span> What your dominant colouring or season is, which colours suit you.</p>
      <p><span class="dot">•</span> How to select colour for garments to enhance your colouring and flatter your body shape.</p>
      <p><span class="dot">•</span> How to select and wear colours to suit your personality and lifestyle.</p>
      <p><span class="dot">•</span> How to coordinate &amp; wear colours in your wardrobe.</p>
      <p><span class="dot">•</span> With a make- up makeover, what makeup colours and shades to select to flatter your colouring, and keep your look current.</p>
      <div class="gap"></div>
      <p>Session:</p>
      <p>Duration - 1 hour 30mins to 2 hours</p>
      <p>Includes – Takeaway a colour swatch of your best colours.</p>
      <p>Information workbook with personalised notes discussed during the consultation.</p>
      <p>Cost &nbsp;&nbsp;$225.00</p>
    </div>
  </section>

  <section class="panel panel--middle">
    <div class="hero-photo" role="img" aria-label="Fashion photo: woman with short blonde hair, white sunglasses and a sleeveless white collared blouse against a turquoise backdrop"></div>
    <svg class="hero-wave" viewBox="0 0 401 60" preserveAspectRatio="none" aria-hidden="true">
      <path d="M0,0 H401 V6 Q220,6 0,34 Z" fill="#2bb3c8"/>
      <path d="M0,34 Q220,6 401,6 V14 Q220,14 0,44 Z" fill="#4a4a4a"/>
      <path d="M0,44 Q220,14 401,14 V60 H0 Z" fill="#c9a33c"/>
    </svg>

    <h2 class="packages-title">Premium Styling Packages</h2>
    <div class="packages">
      <article class="package">
        <h3>Special Occasion Style Me Beautiful Package</h3>
        <p>This is a great experience for weddings, birthdays, or just wanting to look your absolute best for any occasion. Treat someone special to the ultimate gift. Gift vouchers &amp; before and after photos available on request.</p>
        <ul><li>Consultation</li><li>Personal shopping service</li><li>Hair (accompaniment to hair salon)</li><li>Make up Make over</li></ul>
        <p>Price $ 185.00 (This does not include cost of hair salon)</p>
      </article>
      <article class="package">
        <h3>The Forever Gorgeous Package</h3>
        <p>Discover and Sparkle with a new signature style. This package will empower you with the confidence to dress for success every day.</p>
        <ul><li>Style &amp; Colour Consultation</li><li>Personal Shopping Service</li><li>Make up Lesson</li><li>Style me complete consultation (accessories &amp; shoes)</li><li>Hair (accompaniment to hair salon)</li></ul>
        <p>Price $385.00 (This does not include the cost of hair salon)</p>
      </article>
      <article class="package package--compact">
        <h3>The Ultimate Wardrobe Makeover Package</h3>
        <p>This will provide you with a freedom to dress effortlessly for any occasion. Relax and enjoy a functional well-coordinated wardrobe that reflects you and your lifestyle. Discover how to dress without the stress.</p>
        <ul><li>Wardrobe clear out &amp; reassess</li><li>Style &amp; colour consultation</li><li>Style me complete consultation (accessories &amp; shoes)</li></ul>
        <p>Price $365.00</p>
      </article>
    </div>
  </section>

  <section class="panel panel--right">
    <h2 class="script-title">Velvora Make Up Services</h2>
    <div class="services">
      <h3>Special Occasion Make up</h3>
      <p>Get celebrity treatment and have your make up professional applied using expert techniques. Looking good is all about knowing what suits you, when you have your make up professionally applied using the right colours you will reflect a more flawless youthful appearance. You will be sure to look and feel fabulous for that special occasion</p>
      <p>Price: $85.00 per person</p>
      <h3>Make up Lesson</h3>
      <p>Learn how to apply your make up like an expert, during this lesson you will discover how to enhance your features, create a flawless finish and make those eyes sparkle using the colours that flatter you. This session provides hands on process for you to learn the application techquies required to best suit you. Feel confident with the way you apply your make up, and learn how to turn your day look into an evening look.</p>
      <p>Duration Approx. 1.30 to 2 hours</p>
      <p>Price $95.00</p>
      <p>Includes: Take away with you a Makeup Chart with personalized notes on session.</p>
      <h3>Make up Season update</h3>
      <p>Have you been applying your make up the same way for years? Or do you just want to Look and feel confident about your look? Bring your make up bag and we will assess the way you are currently applying your makeup and what colours you are using. We can then work with your existing products and make recommendations to update your look to keep you current.</p>
      <p>Duration: Approx. 1 hour to 1.30mins.</p>
      <p>Price $ 65.00</p>
      <ul class="list">
        <li>Eyebrow shaping $25.00</li>
        <li>Eyelash Tint $18.00</li>
        <li>Eyebrow Tint $15.00</li>
        <li>Eyelash extensions $25.00 (Reusable)</li>
      </ul>
    </div>
    <div class="brand-mark">
      <span class="brand-mark__circle"></span>
      <span class="brand-mark__name">Velvora Style &amp; Image Consultancy</span>
    </div>
  </section>

</main>
</body>
</html>
```